Willowbend Lodge Spring Bookings Email

Will be using Mailwise Relay to send to email list so needs to be formatted correctly. Spring at Willowbend Lodge - featuring the breakfast room (Dawn Kettle Diner) Featuring a free Breakfast Buffet, remodeled rooms and FREE tubing on the river, outdoor pool. All rooms have balconies overlooking the river

Target Market(s)

Guest that have or would like to stay at Willowbend Lodge on the river in pigeon forge..

Industry/Entity Type

Hospitality

Requirements
Must have
• 877.514.2968
• Book now/Reserve Now
• https://thewillowbendlodge.com/
Nice to have
• work in some way to say reserving direct with us is the best rate ->
• The best price is right here!
• We check all of our rates across the web to make sure we have the best prices for guests right here on our website.
• Book now
Should not have
• we are in the SMoky Mountains in Pigeon Forge Tennessee so no references to beaches, etc.

```html
<!DOCTYPE html>
<html lang="en">
<head>
<meta charset="utf-8">
<title>Willowbend Lodge – Spring Bookings</title>
<link rel="stylesheet" href="https://fonts.googleapis.com/css2?family=Montserrat:wght@500;600;700&family=Poppins:wght@400;500&display=swap">
<style>
  :root {
    --page: #f1f1f1;
    --card: #ffffff;
    --ink: #1d1d1d;
    --ink-soft: #6b6b6b;
    --rule: #e4e4e4;
    --brand: #1f7a5c;
    --accent: #f26a4f;
    --pill: #fde3da;
    --dark: #333333;
    --social: #8a97a8;
  }
  * { box-sizing: border-box; margin: 0; padding: 0; }
  html, body { width: 1200px; height: 5325px; overflow: hidden; }
  body {
    background: var(--page);
    font-family: "Poppins", sans-serif;
    color: var(--ink-soft);
    position: relative;
  }
  .abs { position: absolute; }

  .brand { display: flex; align-items: center; gap: 16px; }
  .brand-mark { width: 46px; height: 46px; background: var(--brand); }
  .brand-name { font-family: "Poppins", sans-serif; font-weight: 500; font-size: 34px; color: var(--brand); line-height: 1; }

  .socials { display: flex; gap: 12px; }
  .socials span { width: 46px; height: 46px; border-radius: 50%; background: var(--social); display: block; }
  .socials.square span { border-radius: 0; width: 50px; height: 50px; }

  .topline { left: 153px; right: 153px; top: 89px; height: 2px; background: var(--rule); }
  .utility { top: 255px; font-size: 24px; color: var(--ink-soft); }

  .card { left: 75px; top: 327px; width: 1050px; height: 4963px; background: var(--card); }

  .nav { font-size: 24px; color: var(--ink-soft); display: flex; gap: 18px; }

  .photo { display: block; }
  .pill {
    display: inline-block; background: var(--pill); color: var(--ink);
    font-size: 17px; letter-spacing: 0.5px; padding: 9px 22px; text-transform: uppercase;
  }
  .heading { font-family: "Montserrat", sans-serif; font-weight: 700; color: var(--ink); }
  .body { font-size: 22px; line-height: 36px; }
  .btn {
    display: inline-block; background: var(--accent); color: #fff;
    font-size: 18px; font-weight: 500; padding: 10px 24px; border-radius: 6px; text-transform: uppercase;
  }
  .divider { left: 0; width: 1050px; height: 18px; background: var(--page); }

  .center { text-align: center; left: 0; width: 1050px; }

  .bullets { list-style: none; }
  .bullets li { position: relative; padding-left: 34px; margin-bottom: 34px; font-size: 22px; line-height: 36px; color: var(--accent); }
  .bullets li span { color: var(--ink-soft); }
  .bullets svg { position: absolute; left: 0; top: 10px; }

  .column-title { font-family: "Montserrat", sans-serif; font-weight: 500; font-size: 31px; line-height: 42px; color: var(--ink); }
</style>
</head>
<body>

<!-- Pre-header -->
<div class="abs topline"></div>
<div class="abs brand" style="left:153px; top:144px;">
  <span class="brand-mark"></span><span class="brand-name">Willowbend Lodge</span>
</div>
<div class="abs socials" style="left:813px; top:128px;"><span></span><span></span><span></span><span></span></div>
<div class="abs utility" style="left:153px;">thewillowbendlodge.com</div>
<div class="abs utility" style="left:493px;">Book now / Reserve Now</div>
<div class="abs utility" style="left:880px;">877.514.2968</div>

<main class="abs card">
  <!-- Header -->
  <div class="abs brand" style="left:78px; top:190px;">
    <span class="brand-mark"></span><span class="brand-name">Willowbend Lodge</span>
  </div>
  <nav class="abs nav" style="right:78px; top:146px;"><span>Services</span><span>Products</span><span>Contact Us</span></nav>
  <div class="abs socials" style="right:78px; top:256px;"><span></span><span></span><span></span><span></span></div>

  <div class="abs photo" role="img" aria-label="Guests tubing on the river beside the lodge balconies"
       style="left:0; top:340px; width:1050px; height:700px; background:linear-gradient(180deg,#6f8f5a 0%,#8a7d6a 45%,#9aa3a0 70%,#5f6a58 100%);"></div>

  <!-- Editor's desk -->
  <div class="abs" style="left:78px; top:1110px; width:894px;">
    <span class="pill">From editor's desk</span>
    <h1 class="heading" style="font-size:38px; margin-top:22px;">Spring is here on the river...</h1>
    <p class="body" style="margin-top:18px;">Spring has arrived in Pigeon Forge, and Willowbend Lodge is ready for you. Every room has been remodeled, and every room has a private balcony overlooking the river. Wake to the sound of rushing water and mountain air, then head down for a free breakfast buffet.</p>
    <p class="body" style="margin-top:36px;">The best price is right here! We check all of our rates across the web to make sure we have the best prices for guests right here on our website. Book direct with us for the best rate – call 877.514.2968 or reserve online today.</p>
    <div role="img" aria-label="Handwritten signature" style="margin-top:40px; width:200px; height:56px; background:linear-gradient(90deg,#d9d9d9,#eeeeee);"></div>
  </div>

  <div class="abs divider" style="top:1750px;"></div>

  <!-- Featured services -->
  <div class="abs center" style="top:1845px;">
    <span class="pill">What we do</span>
    <h2 class="heading" style="font-size:37px; margin-top:22px;">OUR FEATURED SERVICES</h2>
    <p class="body" style="margin-top:14px;">Free breakfast, free river tubing and an outdoor pool.<br>All just steps from your balcony on the river.</p>
  </div>

  <!-- Dark feature -->
  <section class="abs" style="left:0; top:2115px; width:1050px; height:895px; background:var(--dark);">
    <div class="abs photo" role="img" aria-label="Remodeled guest room with king bed and television"
         style="left:78px; top:71px; width:894px; height:455px; background:linear-gradient(135deg,#c9b48a 0%,#6a79b8 45%,#4e5f9e 65%,#8a5a38 100%);"></div>
    <div class="abs center" style="top:568px;">
      <span style="font-size:17px; color:#fff; letter-spacing:0.5px; padding-bottom:8px; border-bottom:2px solid #fff;">NEW &amp; POPULAR</span>
      <h2 class="heading" style="font-size:37px; color:#fff; margin-top:24px;">REMODELED RIVERVIEW ROOMS</h2>
      <p class="body" style="color:#e6e6e6; margin:14px auto 0; width:894px;">Fresh furnishings, comfortable beds and a private balcony in every room, each one overlooking the river. Step outside for mountain air and water views.</p>
      <span class="btn" style="margin-top:26px;">Book now</span>
    </div>
  </section>

  <!-- Announcement -->
  <div class="abs photo" role="img" aria-label="River flowing through the forested Smoky Mountains"
       style="left:78px; top:3106px; width:408px; height:635px; background:linear-gradient(180deg,#5d7a4a 0%,#3f5a36 45%,#7e8784 75%,#4d5a48 100%);"></div>
  <div class="abs" style="left:562px; top:3115px; width:410px;">
    <span class="pill">Announcement</span>
    <h3 class="column-title" style="font-size:34px; line-height:44px; margin-top:26px;">Free Tubing on the River This Spring</h3>
    <ul class="bullets" style="margin-top:30px;">
      <li><svg width="18" height="16" viewBox="0 0 18 16"><path d="M1 8h14M9 2l6 6-6 6" fill="none" stroke="currentColor" stroke-width="2"/></svg>Free tubing for every guest, <span>right from our own riverbank.</span></li>
      <li><svg width="18" height="16" viewBox="0 0 18 16"><path d="M1 8h14M9 2l6 6-6 6" fill="none" stroke="currentColor" stroke-width="2"/></svg>Outdoor pool open for spring, <span>with mountain views.</span></li>
      <li><svg width="18" height="16" viewBox="0 0 18 16"><path d="M1 8h14M9 2l6 6-6 6" fill="none" stroke="currentColor" stroke-width="2"/></svg>Best rate when you book direct <span>on our website or by phone.</span></li>
    </ul>
    <span class="btn">Reserve now</span>
  </div>

  <!-- Two columns -->
  <div class="abs photo" role="img" aria-label="Outdoor patio of the breakfast room with yellow tables"
       style="left:78px; top:3862px; width:894px; height:455px; background:linear-gradient(180deg,#5a7a46 0%,#8a6a48 40%,#d9b43a 75%,#8a8a86 100%);"></div>
  <div class="abs" style="left:78px; top:4385px; width:410px;">
    <h3 class="column-title">Dawn Kettle Diner: Free Breakfast Buffet</h3>
    <p class="body" style="margin-top:16px;">A hot breakfast buffet every morning in our breakfast room, free for every guest.</p>
    <span class="btn" style="margin-top:26px;">Read more</span>
  </div>
  <div class="abs" style="left:562px; top:4385px; width:410px;">
    <h3 class="column-title">Best Price Is Right Here on Our Site</h3>
    <p class="body" style="margin-top:16px;">We check our rates across the web so you always get the best price booking direct.</p>
    <span class="btn" style="margin-top:26px;">Book now</span>
  </div>

  <!-- Footer -->
  <div class="abs" style="left:0; top:4712px; width:1050px; height:2px; background:var(--rule);"></div>
  <div class="abs body" style="left:78px; top:4772px;">Unsubscribe | email@website.com</div>
  <div class="abs socials square" style="right:78px; top:4767px;"><span></span><span></span><span></span><span></span><span></span></div>
  <div class="abs" style="left:0; top:4856px; width:1050px; height:2px; background:var(--rule);"></div>
  <div class="abs center" style="top:4893px; font-size:20px;">© N-E-V, 2020. All rights reserved.</div>
</main>

</body>
</html>
```